Business Card Design Project

Hello Designers, hope you are all aiming enjoy the weekend
I have the Business Logo (uploaded), you can alter the color which ever way you think would work,
Im looking for a simple yet striking feel, something which will stay memorable (I have uploaded 3 examples for you to flick through)
Information on the card, will just be the bare minimum,
Double Sided
Info being
i.e.
Name
Number
Website
ABN
Teo Marlowick
+482710365 (singapore)
+615093284 (Australia)
+790428153 (America)
www.lumoren-match.example
ABN 90817263
Enjoy,
Teo

```html
<!DOCTYPE html>
<html lang="en">
<head>
<meta charset="utf-8">
<title>Lumoren Match – Business Card</title>
<link rel="stylesheet" href="https://fonts.googleapis.com/css2?family=Questrial&display=swap">
<style>
  :root {
    --page-bg: #2a2a2b;
    --front-bg: #5e6269;
    --back-bg: #efefef;
    --brand-red: #c1243f;
    --ink-dark: #4e4f52;
    --ink-mid: #5a5b5e;
    --ink-light: #ffffff;
    --fold-dark: rgba(0,0,0,0.35);
    --fold-light: rgba(0,0,0,0);
  }
  * { margin: 0; padding: 0; box-sizing: border-box; }
  html, body {
    width: 1200px; height: 900px; overflow: hidden;
    background: var(--page-bg);
    font-family: "Questrial", "Century Gothic", sans-serif;
  }
  .card {
    position: absolute;
    left: 217px;
    width: 765px;
    height: 420px;
    border-radius: 14px;
    overflow: hidden;
  }
  .card--front { top: 22px; background: var(--front-bg); }
  .card--back { top: 460px; background: var(--back-bg); }
  .fold { position: absolute; inset: 0; width: 100%; height: 100%; }

  .brand-square {
    position: absolute;
    background: var(--brand-red);
    border-radius: 8px;
  }
  .card--front .brand-square { left: 33px; top: 33px; width: 52px; height: 52px; }

  .brand-name {
    position: absolute;
    white-space: nowrap;
    letter-spacing: 0.5px;
  }
  .card--front .brand-name {
    left: 245px; top: 162px;
    font-size: 56px; line-height: 64px;
    color: var(--ink-light);
  }

  .card--back .brand-square { left: 226px; top: 188px; width: 62px; height: 62px; border-radius: 10px; }
  .card--back .brand-name {
    left: 304px; top: 186px;
    font-size: 60px; line-height: 66px;
    color: var(--ink-dark);
  }

  .contact-name {
    position: absolute; left: 38px; top: 40px;
    font-size: 22px; color: var(--ink-dark);
  }
  .contact-list {
    position: absolute; left: 30px; top: 84px;
    list-style: none;
    font-size: 12.5px; color: var(--ink-mid);
  }
  .contact-list li { display: flex; align-items: center; height: 19px; }
  .contact-list svg { width: 12px; height: 12px; margin-right: 7px; }
  .contact-web { position: absolute; left: 30px; top: 158px; font-size: 12.5px; color: var(--ink-mid); display: flex; align-items: center; }
  .contact-web svg { width: 13px; height: 13px; margin-right: 7px; }
  .contact-abn { position: absolute; left: 50px; top: 195px; font-size: 12.5px; color: var(--ink-mid); }
</style>
</head>
<body>

<section class="card card--front" aria-label="Card front">
  <svg class="fold" viewBox="0 0 765 420" preserveAspectRatio="none" aria-hidden="true">
    <defs>
      <linearGradient id="fold-shade-front" x1="1" y1="0" x2="0" y2="0">
        <stop offset="0" stop-color="rgba(0,0,0,0.38)"/>
        <stop offset="0.25" stop-color="rgba(0,0,0,0.12)"/>
        <stop offset="1" stop-color="rgba(0,0,0,0)"/>
      </linearGradient>
    </defs>
    <polygon points="240,0 300,0 155,420 110,420" fill="url(#fold-shade-front)"/>
    <line x1="300" y1="0" x2="155" y2="420" stroke="rgba(255,255,255,0.12)" stroke-width="1"/>
  </svg>
  <div class="brand-square" aria-hidden="true"></div>
  <div class="brand-name">Lumoren Match</div>
</section>

<section class="card card--back" aria-label="Card back">
  <svg class="fold" viewBox="0 0 765 420" preserveAspectRatio="none" aria-hidden="true">
    <defs>
      <linearGradient id="fold-shade-back" x1="1" y1="0" x2="0" y2="0">
        <stop offset="0" stop-color="rgba(0,0,0,0.32)"/>
        <stop offset="0.25" stop-color="rgba(0,0,0,0.08)"/>
        <stop offset="1" stop-color="rgba(0,0,0,0)"/>
      </linearGradient>
    </defs>
    <polygon points="250,0 305,0 148,420 105,420" fill="url(#fold-shade-back)"/>
  </svg>

  <div class="contact-name">Teo Marlowick</div>
  <ul class="contact-list">
    <li><svg viewBox="0 0 12 12"><path fill="#c1243f" d="M1 3.5C1 2 2.5 1.5 6 1.5s5 .5 5 2v1H8.5V3.6H3.5v.9H1zM2.5 5.5h7L11 10.5H1z"/></svg>+482710365 (singapore)</li>
    <li><svg viewBox="0 0 12 12"><path fill="#c1243f" d="M1 3.5C1 2 2.5 1.5 6 1.5s5 .5 5 2v1H8.5V3.6H3.5v.9H1zM2.5 5.5h7L11 10.5H1z"/></svg>+615093284 (Australia)</li>
    <li><svg viewBox="0 0 12 12"><path fill="#c1243f" d="M1 3.5C1 2 2.5 1.5 6 1.5s5 .5 5 2v1H8.5V3.6H3.5v.9H1zM2.5 5.5h7L11 10.5H1z"/></svg>+790428153 (America)</li>
  </ul>
  <div class="contact-web">
    <svg viewBox="0 0 14 14"><g fill="none" stroke="#c1243f" stroke-width="1.2"><circle cx="7" cy="7" r="6"/><ellipse cx="7" cy="7" rx="2.6" ry="6"/><line x1="1" y1="7" x2="13" y2="7"/></g></svg>
    www.lumoren-match.example
  </div>
  <div class="contact-abn">ABN 90817263</div>

  <div class="brand-square" aria-hidden="true"></div>
  <div class="brand-name">Lumoren Match</div>
</section>

</body>
</html>
```